Brightpath Tech Partners Website Design

I have here a website mockup. If you need anything further please feel free to reach out to me! Thank you!

Current site: http://brightpathtechpartners.example/

We want it clean, concise and eye catching.

Menu: I want the same idea we used from lumivexsites.example with the logo in the middle and in the menu:

Home, About Us, How Can We Help?, Media, Blog, Contact Us.

Let's have the Social Media icons at the very top please.

For the banner - we want a pixelharbor chess image sort of like pixelharbor photo 480613927 or 31940287

I want the words "Rise Higher, Run Further, Reach Farther" to come in one at a time and then "Brightpath Tech Partners" to show up on the banner.

Maybe have "Grow Your Business with Managed IT Services from Brightpath Tech Partners" somewhere permanently on the banner that still suits everything.

Services Section: Maybe we can have them as chess pieces with something along the lines of "Make Your Next Move" - Managed IT Services, New Jersey Cloud Computing, Protect Your Business Data, Managed Email Solutions (Background 207946138)

Next Area: What sets us apart?/Testimonials (I want this as a split area) (Can we please use the banner image paralex here?)

(This is for the What Sets Us Apart side)
Outsmart threats before they reach your networks.

Outperform with the newest and latest technologies to not only keep you up and running, but to keep you at an advantage.

Reach Farther by embracing Business Continuity with Brightpath Tech Partners by your side. (I will let you choose the background for here!)

Next Area: Book Your Free Two-Hour Review! (I want a form similar to the one on the old site.)

Next area: Blogs/Sign Up for our newsletter! (Again, please choose a relevant background)

Next Area:Contact Us area with service pages. I really like the contact us part in mordavel.example where it shows the geographical area.

Target Market(s)

Business Owners in New Jersey looking to outsource their business IT, computer and network support.

Industry/Entity Type

Information Technology

Number of Pages Required

1 page

Font styles to use
Sans Serif

Requirements
Must have
• We want this website to be very sharp. I like bright colors, creative imagery.
• In the footer I must have @ 2016 Brightpath Tech Partners | Privacy Policy | Sitemap
Should not have
• I am not a fan of stuffing everything in and making it very busy. I would like clean and professional

```html
<!DOCTYPE html>
<html lang="en">
<head>
<meta charset="utf-8">
<title>Brightpath Tech Partners</title>
<link rel="stylesheet" href="https://fonts.googleapis.com/css2?family=Montserrat:wght@400;600;700&family=Open+Sans:ital,wght@0,400;0,600;0,700;1,400&display=swap">
<style>
:root{
  --blue:#4a9bd5;
  --ink:#222222;
  --text:#555555;
  --muted:#8a8a8a;
  --black:#0d0d0d;
  --white:#ffffff;
  --line:#d9d9d9;
  --panel-grey:#e4e5e7;
  --panel-light:#f1f1f1;
  --footer:#242424;
  --footer-deep:#1b1b1b;
  --footer-text:#c9c9c9;
  --red-stripe:#e0463f;
}
*{box-sizing:border-box;margin:0;padding:0}
html,body{width:1200px;height:2651px;overflow:hidden}
body{font-family:"Open Sans",Arial,sans-serif;color:var(--text);background:var(--white);position:relative}
.section{position:absolute;left:0;width:1200px}
.abs{position:absolute}
.heading{font-family:"Montserrat",Arial,sans-serif;color:var(--ink);font-weight:600}
.accent{color:var(--blue)}
.rule{position:absolute;height:2px;width:46px;background:var(--ink)}

/* top bar */
.topbar{top:0;height:35px;background:var(--black);color:var(--white);font-size:13px}
.topbar .phone{left:99px;top:8px;display:flex;align-items:center;gap:8px}
.social{display:flex;gap:6px}
.social span{width:18px;height:18px;border:1px solid currentColor;display:block}
.topbar .social{right:99px;top:8px}

/* nav */
.nav{top:35px;height:59px;background:var(--white);border-bottom:1px solid var(--line);font-size:12px;font-weight:700;color:var(--ink)}
.nav a{position:absolute;top:22px;color:var(--ink);text-decoration:none}
.nav a.current{color:var(--blue)}
.nav a.current::after{content:"";position:absolute;left:-6px;right:-6px;top:30px;height:3px;background:var(--blue)}
.nav .sep{position:absolute;top:20px;color:#b5b5b5;font-size:14px}
.brand-tab{left:450px;top:0;width:300px;height:94px;z-index:3}
.brand{position:absolute;left:0;right:0;top:36px;display:flex;justify-content:center;align-items:center;gap:8px;font-family:"Open Sans",Arial,sans-serif;font-weight:700;font-size:19px;color:var(--ink)}
.brand i{width:22px;height:22px;border-radius:50%;background:var(--blue);display:block}

/* hero */
.hero{top:94px;height:512px;background:radial-gradient(ellipse at 50% 35%,#5b7283 0%,#27323b 45%,#07090b 100%)}
.hero .title{left:0;width:1200px;top:232px;text-align:center;color:var(--white);font-size:44px;font-weight:600}
.hero .title-rule{left:435px;top:292px;width:330px;height:1px;background:rgba(255,255,255,.6)}
.hero .sub{left:0;width:1200px;top:310px;text-align:center;color:var(--white);font-size:24px;font-weight:700;line-height:35px}
.slide-arrow{top:263px;width:33px;height:33px;border:1px solid rgba(255,255,255,.6);background:rgba(0,0,0,.3)}
.slide-arrow svg{display:block}

/* services */
.services{top:606px;height:447px;background:linear-gradient(180deg,#d9dadc,#eceded 50%,#dedfe1)}
.section-title{left:0;width:1200px;text-align:center;font-size:32px}
.services .tagline{left:0;width:1200px;top:105px;text-align:center;font-size:13px;font-weight:700;color:var(--ink)}
.service{width:230px;text-align:center}
.service .badge{width:117px;height:117px;margin:0 auto;border-radius:50%;background:linear-gradient(160deg,#f4f4f4,#9a9a9a);padding:8px;box-shadow:0 4px 8px rgba(0,0,0,.25)}
.service .badge div{width:101px;height:101px;border-radius:50%;background:radial-gradient(circle at 50% 35%,#3a3a3a,#050505);display:flex;align-items:center;justify-content:center}
.service h3{margin-top:26px;font-size:16px;line-height:23px;font-weight:700;color:var(--ink)}
.service p{margin-top:10px;font-size:13px;line-height:25px}
.service .more{width:22px;height:22px;background:var(--black);color:var(--white);margin:10px auto 0;display:flex;align-items:center;justify-content:center;font-weight:700;font-size:18px;line-height:1}

/* testimonials */
.testimonials{top:1053px;height:361px;background:var(--panel-light)}
.testimonials h2{left:99px;top:46px;font-size:26px}
.pager{top:52px;display:flex;gap:6px}
.pager span{width:22px;height:22px;border:1px solid #9bb8cf;display:flex;align-items:center;justify-content:center;color:var(--blue);font-size:12px}
.avatar{left:102px;top:120px;width:145px;height:145px;border-radius:50%;background:linear-gradient(150deg,#d7dbe0,#7f8a96);border:5px solid var(--white);box-shadow:0 0 0 1px var(--line)}
.client-name{left:99px;width:156px;top:278px;text-align:center;font-size:13px;font-weight:700;color:var(--ink)}
.quote{left:265px;top:186px;width:300px;font-size:12px;line-height:23px;font-style:italic;color:var(--text)}
.quote-mark{font-family:Georgia,serif;font-size:30px;color:#bbb;font-style:normal}
.video{left:672px;top:55px;width:397px;height:247px;background:linear-gradient(120deg,#e8ecef,#b7c2cc 55%,#8c98a5);border:6px solid var(--white);box-shadow:0 6px 14px rgba(0,0,0,.25)}
.play{left:162px;top:84px;width:62px;height:62px;border-radius:50%;background:rgba(0,0,0,.55);display:flex;align-items:center;justify-content:center}

/* review form */
.review{top:1414px;height:282px;background:var(--panel-grey)}
.review h2{left:99px;top:40px;font-size:26px;line-height:34px;font-weight:600;letter-spacing:.3px}
.review .intro{left:99px;top:116px;width:360px;font-size:13px;line-height:20.5px}
.review h3{left:511px;top:42px;font-size:24px}
.field{background:var(--white);border:1px solid #d2d2d2;height:42px;font-size:12px;color:var(--muted);padding:13px 14px}
.field-label{left:511px;top:190px;font-size:12px;color:var(--text)}
.select{display:flex;justify-content:space-between;align-items:center;padding:0 0 0 14px}
.select b{width:30px;border-left:1px solid #ddd;height:28px;display:flex;align-items:center;justify-content:center;font-size:10px;color:#888;font-weight:400}
.submit{left:816px;top:203px;width:119px;height:39px;background:var(--blue);color:var(--white);font-size:13px;display:flex;align-items:center;justify-content:center}

/* blog */
.blog{top:1696px;height:363px;background:#f6f6f6}
.post{top:124px;width:472px;height:189px;background:var(--white);border:1px solid var(--line);border-top:2px solid var(--blue)}
.post .thumb{left:0;top:0;width:189px;height:187px;background:linear-gradient(135deg,#c3ccd3,#6d7c89)}
.post .date{left:143px;top:0;width:46px;height:46px;background:var(--blue);color:var(--white);text-align:center;font-weight:700;font-size:15px;line-height:17px;padding-top:5px}
.post .date small{display:block;font-size:10px;font-weight:400}
.post h4{left:200px;top:10px;font-size:16px;color:var(--ink);font-weight:700}
.post p{left:200px;top:38px;width:262px;font-size:12px;line-height:22px}
.post .meta{left:189px;top:140px;right:0;height:47px;border-top:1px solid var(--line);display:flex;align-items:center;font-family:"Montserrat",Arial,sans-serif;font-size:13px;color:var(--ink)}
.post .meta span{padding:0 11px}
.post .meta span+span{border-left:1px solid var(--line)}

/* newsletter */
.newsletter{top:2059px;height:198px;background:#ebe8e2}
.signup{left:127px;top:44px;width:951px;height:111px;background:#f1f1ee;border-top:5px solid var(--red-stripe);border-bottom:5px solid var(--red-stripe)}
.signup h2{left:85px;top:34px;font-size:22px}
.signup .email{left:421px;top:34px;width:367px;height:36px;font-size:12px;padding:10px 12px;color:var(--muted)}
.signup .subscribe{left:801px;top:34px;width:122px;height:36px;background:var(--blue);color:var(--white);font-size:12px;font-weight:700;display:flex;align-items:center;justify-content:center}

/* footer */
.footer{top:2257px;height:344px;background:var(--footer)}
.footer h5{top:64px;font-family:"Montserrat",Arial,sans-serif;color:var(--white);font-size:19px;font-weight:600}
.footer .col-rule{top:105px;height:1px;background:#3c3c3c}
.footer .divider{top:64px;width:1px;height:230px;background:#3a3a3a}
.links{left:99px;top:98px;list-style:none;font-size:12px;color:var(--footer-text)}
.links li{height:30px;display:flex;align-items:center;gap:14px}
.links li::before{content:"";width:5px;height:5px;border-radius:50%;background:var(--white)}
.contact{left:311px;top:106px;font-size:12px;color:var(--footer-text);line-height:21px}
.contact .row{display:flex;gap:14px;margin-bottom:18px}
.contact svg{flex:none;margin-top:4px}
.contact strong{color:var(--white)}
.map{left:603px;top:104px;width:195px;height:195px;border-radius:50%;background:radial-gradient(circle,#f2efe4,#d9d2bf 70%,#a9b7c6);border:6px solid #cfcfcf}
.foot-brand{left:870px;top:168px;width:232px;display:flex;align-items:center;gap:8px;justify-content:center;font-weight:700;font-size:19px;color:var(--white)}
.foot-brand i{width:22px;height:22px;border-radius:50%;background:#8e8e8e;display:block}
.footer .social{left:918px;top:256px;color:var(--white)}
.copyright{top:2601px;height:50px;background:var(--footer-deep);color:#8e8e8e;font-size:12px;text-align:center;line-height:50px}
</style>
</head>
<body>

<header class="section topbar">
  <div class="abs phone">
    <svg width="14" height="14" viewBox="0 0 24 24"><path d="M6.6 10.8a15.1 15.1 0 0 0 6.6 6.6l2.2-2.2c.3-.3.7-.4 1-.2 1.1.4 2.3.6 3.6.6.6 0 1 .4 1 1V20c0 .6-.4 1-1 1A17 17 0 0 1 3 4c0-.6.4-1 1-1h3.5c.6 0 1 .4 1 1 0 1.3.2 2.5.6 3.6.1.3 0 .7-.2 1z" fill="#fff"/></svg>
    Phone: (555) 014-2290
  </div>
  <div class="abs social" aria-label="Social media links"><span></span><span></span><span></span><span></span><span></span></div>
</header>

<nav class="section nav">
  <a class="current" style="left:112px">Home</a>
  <span class="sep" style="left:170px">»</span>
  <a style="left:204px">About Us</a>
  <span class="sep" style="left:282px">»</span>
  <a style="left:316px">How Can We Help?</a>
  <a style="left:767px">Media</a>
  <span class="sep" style="left:846px">»</span>
  <a style="left:899px">Blog</a>
  <span class="sep" style="left:966px">»</span>
  <a style="left:1022px">Contact Us</a>
</nav>
<div class="abs brand-tab">
  <svg class="abs" width="300" height="94" viewBox="0 0 300 94" style="left:0;top:0"><path d="M22 0H278L300 35V94H0V35Z" fill="#fff"/></svg>
  <div class="brand"><i></i>Brightpath Tech Partners</div>
</div>

<section class="section hero" role="img" aria-label="Glass chess pieces and businessmen standing on a reflective chessboard">
  <div class="abs slide-arrow" style="left:48px"><svg width="31" height="31" viewBox="0 0 31 31"><path d="M18 9l-6 6.5 6 6.5" stroke="#fff" stroke-width="1.6" fill="none"/></svg></div>
  <div class="abs slide-arrow" style="right:48px"><svg width="31" height="31" viewBox="0 0 31 31"><path d="M13 9l6 6.5-6 6.5" stroke="#fff" stroke-width="1.6" fill="none"/></svg></div>
  <h1 class="abs title">Brightpath Tech Partners</h1>
  <div class="abs title-rule"></div>
  <p class="abs sub">Grow Your Business with Managed IT Services from<br>Brightpath Tech Partners</p>
</section>

<section class="section services">
  <h2 class="abs heading section-title" style="top:44px">Our <span class="accent">Services</span></h2>
  <div class="rule" style="left:577px;top:92px"></div>
  <p class="abs tagline">Make Your Next Move</p>

  <div class="abs service" style="left:99px;top:149px">
    <div class="badge"><div>
      <svg width="48" height="48" viewBox="0 0 48 48" fill="none" stroke="#fff" stroke-width="2"><circle cx="24" cy="12" r="5" fill="#fff"/><path d="M24 17v9M10 34l14-8 14 8M24 26v10"/><circle cx="9" cy="37" r="4"/><circle cx="24" cy="39" r="4"/><circle cx="39" cy="37" r="4"/></svg>
    </div></div>
    <h3>Managed<br>IT Services</h3>
    <p>Lorem ipsum dolor sit amet,<br>consectetuer adipiscing elit, sed diam</p>
    <div class="more">+</div>
  </div>

  <div class="abs service" style="left:357px;top:149px">
    <div class="badge"><div>
      <svg width="52" height="48" viewBox="0 0 52 48" fill="none" stroke="#fff" stroke-width="2"><path d="M14 22a9 9 0 0 1 1-16 11 11 0 0 1 21 2 8 8 0 0 1 2 14z"/><path d="M26 22v6M12 28h28M12 28v4M40 28v4"/><rect x="5" y="32" width="14" height="9"/><rect x="33" y="32" width="14" height="9"/><path d="M3 44h18M31 44h18"/></svg>
    </div></div>
    <h3>New Jersey<br>Cloud Computing</h3>
    <p>Lorem ipsum dolor sit amet,<br>consectetuer adipiscing elit, sed diam</p>
    <div class="more">+</div>
  </div>

  <div class="abs service" style="left:613px;top:149px">
    <div class="badge"><div>
      <svg width="48" height="48" viewBox="0 0 48 48" fill="#fff"><ellipse cx="20" cy="10" rx="14" ry="5"/><path d="M6 14c0 3 6 5 14 5s14-2 14-5v7c0 3-6 5-14 5S6 24 6 21z"/><path d="M6 25c0 3 6 5 14 5 2 0 4 0 6-.5V37c-2 .4-4 .5-6 .5-8 0-14-2-14-5z"/><circle cx="35" cy="34" r="6" fill="none" stroke="#fff" stroke-width="2.5"/><path d="M39 38l6 6" stroke="#fff" stroke-width="3"/></svg>
    </div></div>
    <h3>Protect Your<br>Business Data</h3>
    <p>Lorem ipsum dolor sit amet,<br>consectetuer adipiscing elit, sed diam</p>
    <div class="more">+</div>
  </div>

  <div class="abs service" style="left:862px;top:149px">
    <div class="badge"><div>
      <svg width="52" height="44" viewBox="0 0 52 44" fill="none" stroke="#fff" stroke-width="2"><path d="M12 34a10 10 0 0 1-1-20 14 14 0 0 1 27-2 11 11 0 0 1 3 22z"/><rect x="16" y="19" width="20" height="13"/><path d="M16 19l10 8 10-8"/></svg>
    </div></div>
    <h3>Managed Email<br>Solutions</h3>
    <p>Lorem ipsum dolor sit amet,<br>consectetuer adipiscing elit, sed diam</p>
    <div class="more">+</div>
  </div>
</section>

<section class="section testimonials">
  <h2 class="abs heading">Client <span class="accent">Testimonials</span></h2>
  <div class="rule" style="left:99px;top:98px"></div>
  <div class="abs pager" style="left:506px"><span>‹</span><span>›</span></div>
  <div class="abs avatar" role="img" aria-label="Portrait of the client giving the testimonial"></div>
  <p class="abs client-name">- Marlo Quent</p>
  <p class="abs quote"><span class="quote-mark">“</span> Lorem ipsumn sit amet co adipiscli tsedudml eiusmo dtepor incidiunt ut la dolore ma aliquanmi kni enim nim veni exercitation ullamco ips sdltinol ameti co adipiscig elitsed do eiusmod. <span class="quote-mark">”</span></p>
  <div class="abs video" role="img" aria-label="Video still of a team meeting around a presenter at a whiteboard">
    <div class="abs play"><svg width="22" height="24" viewBox="0 0 22 24"><path d="M3 2l17 10L3 22z" fill="#fff"/></svg></div>
  </div>
</section>

<section class="section review">
  <h2 class="abs heading">Book Your Free Two-Hour<br><span class="accent">Review!</span></h2>
  <p class="abs intro">Lorem ipsum dolor sit amet, consectetuer adipiscing elit, sed diam nonummy nibh euismod tincidunt ut laoreet dolore magna aliquam erat volutpat. Ut wisi enim ad minim veniam, quis nostrud exerci tation ullamcorper suscipit lobortis nisl ut aliquip ex ea commodo consequat. Duis autem vel eum iriure dolor in hendrerit in vulputate</p>
  <h3 class="abs heading">Get Started <span class="accent">Now!</span></h3>
  <div class="abs field" style="left:511px;top:81px;width:281px">Full Name</div>
  <div class="abs field" style="left:816px;top:81px;width:283px">Company</div>
  <div class="abs field" style="left:511px;top:132px;width:281px">Phone</div>
  <div class="abs field" style="left:816px;top:132px;width:283px">Email</div>
  <p class="abs field-label">How can our team help you?*</p>
  <div class="abs field select" style="left:511px;top:203px;width:281px;height:44px">Select One<b>▼</b></div>
  <div class="abs submit">Submit</div>
</section>

<section class="section blog">
  <h2 class="abs heading section-title" style="top:44px">Our <span class="accent">Blog</span></h2>
  <div class="rule" style="left:577px;top:96px"></div>

  <article class="abs post" style="left:99px">
    <div class="abs thumb" role="img" aria-label="Businessmen reviewing work at a computer in an office"></div>
    <div class="abs date">18<small>Sep</small></div>
    <h4 class="abs">Lorem ipsum dolor sit amet,</h4>
    <p class="abs">veniam, quis nostrud exerci tation corper suscipit lobortis nisl ut aliquip ex ea tmodo consequat. Duis autem vel eum iriure dolor in hendrerit in vulputate velit esse,</p>
    <div class="abs meta"><span>By: Corvin Hale</span><span>Read More »</span></div>
  </article>

  <article class="abs post" style="left:627px">
    <div class="abs thumb" role="img" aria-label="Smiling colleagues looking at a laptop together"></div>
    <div class="abs date">18<small>Sep</small></div>
    <h4 class="abs">Duis autem vel eum iriure</h4>
    <p class="abs">Ut wisi enim ad minim veniam, quis strud exerci tation ullamcorper suscipit lobortis nisl ut aliquip ex ea commodo consequat. Duis autem vel eum iriure dolor,</p>
    <div class="abs meta"><span>By: Corvin Hale</span><span>Read More »</span></div>
  </article>
</section>

<section class="section newsletter">
  <div class="abs signup">
    <svg class="abs" style="left:4px;top:18px" width="68" height="66" viewBox="0 0 68 66" fill="none" stroke="#c9c9c9" stroke-width="2"><path d="M4 24L34 4l30 20v38H4z"/><path d="M4 24l30 22 30-22M4 62l24-20M64 62L40 42"/></svg>
    <h2 class="abs heading">Sign Up For Newsletter</h2>
    <div class="abs field email">Enter email address</div>
    <div class="abs subscribe">SUBSCIBE</div>
  </div>
</section>

<footer class="section footer">
  <h5 class="abs" style="left:99px">Quick Links</h5>
  <ul class="abs links">
    <li>Home</li><li>About Us</li><li>How Can We Help?</li><li>Media</li><li>Blog</li><li>Contact Us</li>
  </ul>
  <div class="abs divider" style="left:270px"></div>

  <h5 class="abs" style="left:311px">Contact Us</h5>
  <div class="abs col-rule" style="left:311px;width:215px"></div>
  <div class="abs contact">
    <div class="row"><svg width="11" height="15" viewBox="0 0 12 16"><path d="M6 0a6 6 0 0 1 6 6c0 4-6 10-6 10S0 10 0 6a6 6 0 0 1 6-6z" fill="#fff"/><circle cx="6" cy="6" r="2.2" fill="#242424"/></svg><div>Brightpath Tech Partners<br>48 Alder Lane,<br>Fairview NJ 07099</div></div>
    <div class="row"><svg width="12" height="12" viewBox="0 0 24 24"><path d="M6.6 10.8a15.1 15.1 0 0 0 6.6 6.6l2.2-2.2c.3-.3.7-.4 1-.2 1.1.4 2.3.6 3.6.6.6 0 1 .4 1 1V20c0 .6-.4 1-1 1A17 17 0 0 1 3 4c0-.6.4-1 1-1h3.5c.6 0 1 .4 1 1 0 1.3.2 2.5.6 3.6.1.3 0 .7-.2 1z" fill="#fff"/></svg><strong>(555) 014-2290</strong></div>
    <div class="row"><svg width="13" height="10" viewBox="0 0 13 10"><rect width="13" height="10" fill="#fff"/><path d="M0 0l6.5 5L13 0" stroke="#242424" fill="none"/></svg><div>contactus@brightpathtech.example</div></div>
  </div>
  <div class="abs divider" style="left:571px"></div>

  <h5 class="abs" style="left:603px">Our Location</h5>
  <div class="abs col-rule" style="left:603px;width:190px"></div>
  <div class="abs map" role="img" aria-label="Circular street map marking the office location"></div>

  <div class="abs foot-brand"><i></i>Brightpath Tech Partners</div>
  <div class="abs social" aria-label="Social media links"><span></span><span></span><span></span><span></span><span></span></div>
</footer>

<div class="section copyright">Copyright © 2016 Brightpath Tech Partners. All Rights Reserved</div>

</body>
</html>
```